Business card for Sports Apparel business

DOUBLE SIDED DESIGN
We need business cards for a new sports apparel business. We are developing a protective headband for soccer initially.
Corvell is focused on designing and developing head protection products to reduce the likelihood of concussion when playing sports. Exploring and understanding medical insights, material science research, current and former players experiences and governing bodies guidelines has allowed Corvell to develop the safety, style, form and function requirements of a suitable product to bring to market.
Target Market(s)
Mums buying kits for the sons and daughters. Amateur footballers.
Industry/Entity Type
Sporting Good
Contact Information for Business Card
Martin Ashgrove - CEO
Mobile: +44 7391608254
Email: martin@corvell.co.uk
Tel: 0208 5143927
Helena Pardoe - COO
Mob: +44 7356 409183
Email: helena@corvell.co.uk
Tel: 0208 5143927
Duncan Wyvern - CCO
Mob: +44 7468 230517
Email: duncan@corvell.co.uk
Tel: 0208 5143927
Look and feel

```html
<!DOCTYPE html>
<html lang="en">
<head>
<meta charset="utf-8">
<title>Corvell – Business Card</title>
<link rel="stylesheet" href="https://fonts.googleapis.com/css2?family=Source+Sans+3:wght@400;600;700&display=swap">
<style>
  :root {
    --page-bg: #e9eaec;
    --card-bg: #ffffff;
    --brand-blue: #0d549c;
    --ink-grey: #414345;
    --on-blue: #ffffff;
  }
  * { box-sizing: border-box; margin: 0; padding: 0; }
  html, body {
    width: 1200px;
    height: 1116px;
    overflow: hidden;
    background: var(--page-bg);
    font-family: "Source Sans 3", "Myriad Pro", Arial, sans-serif;
  }
  .card {
    position: absolute;
    left: 100px;
    top: 238px;
    width: 1000px;
    height: 640px;
    background: var(--card-bg);
    box-shadow: 0 18px 40px rgba(0, 0, 0, 0.12);
  }
  .brand-name {
    position: absolute;
    left: 110px;
    top: 348px;
    font-size: 96px;
    font-weight: 600;
    letter-spacing: 2px;
    color: var(--ink-grey);
    line-height: 1;
  }
  .contact-panel {
    position: absolute;
    left: 560px;
    top: 100px;
    width: 400px;
    height: 310px;
    background: var(--brand-blue);
    border-radius: 20px;
    color: var(--on-blue);
    padding: 34px 34px 0 44px;
  }
  .person-name {
    font-size: 36px;
    font-weight: 700;
    line-height: 1.05;
  }
  .person-role {
    font-size: 32px;
    font-weight: 400;
    line-height: 1.1;
  }
  .divider {
    height: 2px;
    background: var(--on-blue);
    margin: 14px 0 22px;
  }
  .contact-list { list-style: none; }
  .contact-item {
    display: flex;
    align-items: center;
    gap: 14px;
    font-size: 30px;
    line-height: 1;
    margin-bottom: 16px;
  }
  .contact-icon {
    flex: none;
    width: 30px;
    height: 30px;
  }
</style>
</head>
<body>
  <div class="card">
    <div class="brand-name">CORVELL</div>

    <div class="contact-panel">
      <p class="person-name">Martin Ashgrove</p>
      <p class="person-role">CEO</p>
      <div class="divider"></div>
      <ul class="contact-list">
        <li class="contact-item">
          <svg class="contact-icon" viewBox="0 0 30 30" aria-hidden="true">
            <circle cx="15" cy="15" r="15" fill="#fff"/>
            <rect x="10" y="6" width="10" height="18" rx="2" fill="none" stroke="var(--brand-blue)" stroke-width="2"/>
            <circle cx="15" cy="21" r="1.2" fill="var(--brand-blue)"/>
          </svg>
          <span>+44 7391608254</span>
        </li>
        <li class="contact-item">
          <svg class="contact-icon" viewBox="0 0 30 30" aria-hidden="true">
            <circle cx="15" cy="15" r="15" fill="#fff"/>
            <rect x="7" y="9" width="16" height="12" fill="none" stroke="var(--brand-blue)" stroke-width="2"/>
            <path d="M7 9 L15 16 L23 9" fill="none" stroke="var(--brand-blue)" stroke-width="2"/>
          </svg>
          <span>martin@corvell.co.uk</span>
        </li>
        <li class="contact-item">
          <svg class="contact-icon" viewBox="0 0 30 30" aria-hidden="true">
            <circle cx="15" cy="15" r="15" fill="#fff"/>
            <path d="M11 8 C9 9 8 11 9 14 C10 18 13 21 17 22 C19 22.5 21 21.5 22 20 L19 17.5 L17 19 C15 18 12.5 15.5 11.5 13.5 L13 11.5 Z" fill="var(--brand-blue)"/>
          </svg>
          <span>0208 5143927</span>
        </li>
      </ul>
    </div>
  </div>
</body>
</html>
```